Neues Design für unseren Wandkalender 2025 Illustrationen für den Kalenderkopf
Mit großer Kreativität und einem Auge für Details hat morlinkas ein Design geschaffen, das nicht nur visuell beeindruckt, sondern auch perfekt die Werte und Atmosphäre unseres Unternehmens einfängt. Der Entwurf hebt sich durch die gelungene Kombination von Ästhetik und Funktionalität ab und bringt die verschiedenen Elemente harmonisch zusammen. Die frischen Farben und modernen Linien verleihen dem Kalenderkopf einen einzigartigen Look, der zugleich zeitlos und stilvoll ist. Besonders beeindruckt waren wir davon, wie gut das Design das Thema des kommenden Jahres aufgreift und eine einladende, positive Stimmung vermittelt. Das Ergebnis ist nicht nur eine Augenweide, sondern auch eine Bereicherung für alle, die mit dem Kalender 2025 arbeiten werden. Ein großes Dankeschön an morlinkas für die hervorragende Arbeit und den inspirierenden Beitrag zum Kalenderprojekt! Wir sind sicher, dass das Design das Jahr 2025 für uns alle noch schöner machen wird.
Zielgruppe
Wir sind die Halvers Datentechnik GmbH aus Leipzig. Mit über 20 Jahren Erfahrung im Bereich Softwareentwicklung gestalten und entwickeln wir moderne Applikationen aus der Sichtweise des Anwenders.
Das grundlegende lösungsorientierte Konzept entwickeln wir gemeinsam im Dialog. Ergebnis ist eine individuelle, bedienerfreundliche Software in einem ansprechenden Design.
Aufgabenstellung
Liebe Illustratorinnen und Illustratoren,
wir sind begeistert von Kreativität und Originalität und suchen nach talentierten Illustratorinnen und Illustratoren, die uns bei diesem aufregenden Projekt unterstützen möchten. Der Wandkalender soll unsere Marke repräsentieren und unseren Kunden ein einzigartiges visuelles Erlebnis bieten.
Da die Motivfindung im letzten Jahr schwierig war, haben wir beschlossen, das Thema in diesem Jahr auf ein konkretes Produkt einzuschränken: Pluvio! Fuhrparkmanagement
Inhalte zum Produkt unter: https://hdt-beispielwerk.de/produkte/pluvio-fuhrparkmanagement/
Pluvio! Fuhrparkmanagement – Ihre intelligente Lösung zur effizienten Verwaltung des betrieblichen Fuhrparks. Mit dieser innovativen Software behalten Sie stets den Überblick über Fahrzeugdaten, Fahrerinformationen und Vertragsdetails. Ob Bestellungen, Dokumentenmanagement oder die Verwaltung von Leasingverträgen und Tankkarten – Pluvio! bietet Ihnen alle Funktionen, die Sie für eine reibungslose und kosteneffiziente Fuhrparksteuerung benötigen. Einfach in der Anwendung, umfassend in den Möglichkeiten, sorgt Pluvio! für optimierte Prozesse und eine perfekte Organisation.
Nährere Infos: siehe Word-Dokument

```html
<!DOCTYPE html>
<html lang="de">
<head>
<meta charset="utf-8">
<title>Wandkalender 2025 – Halvers Datentechnik</title>
<link href="https://fonts.googleapis.com/css2?family=Dosis:wght@500;600;700;800&display=swap" rel="stylesheet">
<style>
  :root{
    --orange:#e8791e;
    --slate:#3d4446;
    --ink:#2f3436;
    --day:#5d6366;
    --weekend-bg:#d8dadb;
    --weekend-ink:#9ea3a6;
    --kw:#b4b8bb;
    --rule:#e4e6e7;
    --paper:#ffffff;
  }
  *{box-sizing:border-box}
  html,body{margin:0;width:1200px;height:801px;overflow:hidden;background:var(--paper)}
  .calendar{position:relative;width:1200px;height:801px;font-family:"Dosis",sans-serif;color:var(--ink)}

  /* header */
  .brand{position:absolute;left:20px;top:52px;display:flex;flex-direction:column;gap:3px}
  .brand-name{font-weight:800;font-size:38px;line-height:1;color:var(--ink);letter-spacing:1px}
  .brand-sub{font-weight:700;font-size:10.5px;color:var(--ink);letter-spacing:.2px}
  .brand-divider{position:absolute;left:199px;top:38px;width:1px;height:70px;background:#9aa0a3}
  .product{position:absolute;left:220px;top:58px;font-weight:700;font-size:34px;color:var(--ink);line-height:1}
  .header-art{position:absolute;left:366px;top:24px;width:580px;height:142px;
    background:linear-gradient(100deg,#ffffff 0%,#fdeede 45%,#fbe2c8 100%);border-radius:4px}
  .year{position:absolute;right:18px;top:40px;font-weight:800;font-size:92px;line-height:1;letter-spacing:-2px}
  .year .accent{color:var(--orange)}
  .url{position:absolute;right:18px;top:135px;font-size:10px;color:var(--orange);font-weight:600}

  /* month bar */
  .month-bar{position:absolute;left:0;top:165px;width:1200px;height:32px;background:var(--slate)}
  .month-bar span{position:absolute;top:2px;color:#fff;font-size:12px;line-height:13px;font-weight:500;padding-left:10px}
  .month-bar span::before{content:"";position:absolute;left:0;top:1px;width:6px;height:6px;background:var(--orange)}

  /* grid */
  .grid{position:absolute;left:18px;top:198px;display:grid;grid-template-columns:repeat(14,83px)}
  .month{list-style:none;margin:0;padding:0;display:grid;grid-template-rows:repeat(31,19.4px);border-left:1px solid var(--rule)}
  .month li{position:relative;display:flex;align-items:center;padding-left:4px;border-bottom:1px solid #fff;
    box-shadow:inset 0 -1px 0 var(--rule);font-weight:500;font-size:15px;line-height:1;color:var(--day)}
  .month li i{font-style:normal;font-size:7.5px;align-self:flex-start;margin:3px 0 0 1px}
  .month li.we{background:var(--weekend-bg);color:var(--weekend-ink)}
  .month li.hol{color:var(--orange)}
  .month li s{text-decoration:none;position:absolute;left:18px;bottom:1px;font-size:4.6px;white-space:nowrap}
  .month li b{position:absolute;right:4px;top:0;font-weight:700;font-size:33px;line-height:1;color:var(--kw);z-index:1}
</style>
</head>
<body>
<div class="calendar">
  <header>
    <div class="brand">
      <span class="brand-name">HDT</span>
      <span class="brand-sub">HALVERS DATENTECHNIK</span>
    </div>
    <div class="brand-divider"></div>
    <div class="product">Pluvio!</div>
    <div class="header-art" role="img" aria-label="Illustration: Frau vor einem Terminplaner, Auto, Sanduhr und Smartphone mit Standort-Pin auf einer geschwungenen Linie"></div>
    <div class="year"><span class="accent">20</span>25</div>
    <div class="url">www.hdt-beispielwerk.de</div>
  </header>

  <nav class="month-bar">
    <span style="left:20px">Dezember<br>2022</span>
    <span style="left:103px">Januar</span>
    <span style="left:186px">Februar</span>
    <span style="left:269px">März</span>
    <span style="left:352px">April</span>
    <span style="left:435px">Mai</span>
    <span style="left:518px">Juni</span>
    <span style="left:601px">Juli</span>
    <span style="left:684px">August</span>
    <span style="left:767px">September</span>
    <span style="left:850px">Oktober</span>
    <span style="left:933px">November</span>
    <span style="left:1016px">Dezember</span>
    <span style="left:1099px">Januar<br>2024</span>
  </nav>

  <main class="grid">
    <!-- Dezember 2022 -->
    <ul class="month">
      <li>1<i>Do</i><b>48</b></li><li>2<i>Fr</i></li><li class="we">3<i>Sa</i></li><li class="we">4<i>So</i></li>
      <li>5<i>Mo</i><b>49</b></li><li>6<i>Di</i></li><li>7<i>Mi</i></li><li>8<i>Do</i></li><li>9<i>Fr</i></li>
      <li class="we">10<i>Sa</i></li><li class="we">11<i>So</i></li>
      <li>12<i>Mo</i><b>50</b></li><li>13<i>Di</i></li><li>14<i>Mi</i></li><li>15<i>Do</i></li><li>16<i>Fr</i></li>
      <li class="we">17<i>Sa</i></li><li class="we">18<i>So</i></li>
      <li>19<i>Mo</i><b>51</b></li><li>20<i>Di</i></li><li>21<i>Mi</i></li><li>22<i>Do</i></li><li>23<i>Fr</i></li>
      <li class="we">24<i>Sa</i><s>Heiligabend</s></li><li class="we hol">25<i>So</i><s>1. Weihnachtstag</s></li>
      <li class="hol">26<i>Mo</i><s>2. Weihnachtstag</s></li><li>27<i>Di</i><b>52</b></li><li>28<i>Mi</i></li><li>29<i>Do</i></li><li>30<i>Fr</i></li>
      <li class="we">31<i>Sa</i><s>Silvester</s></li>
    </ul>
    <!-- Januar -->
    <ul class="month">
      <li class="we hol">1<i>So</i><s>Neujahr</s></li>
      <li>2<i>Mo</i><b>1</b></li><li>3<i>Di</i></li><li>4<i>Mi</i></li><li>5<i>Do</i></li><li class="hol">6<i>Fr</i><s>Heilige Drei Könige *</s></li>
      <li class="we">7<i>Sa</i></li><li class="we">8<i>So</i></li>
      <li>9<i>Mo</i><b>2</b></li><li>10<i>Di</i></li><li>11<i>Mi</i></li><li>12<i>Do</i></li><li>13<i>Fr</i></li>
      <li class="we">14<i>Sa</i></li><li class="we">15<i>So</i></li>
      <li>16<i>Mo</i><b>3</b></li><li>17<i>Di</i></li><li>18<i>Mi</i></li><li>19<i>Do</i></li><li>20<i>Fr</i></li>
      <li class="we">21<i>Sa</i></li><li class="we">22<i>So</i></li>
      <li>23<i>Mo</i><b>4</b></li><li>24<i>Di</i></li><li>25<i>Mi</i></li><li>26<i>Do</i></li><li>27<i>Fr</i></li>
      <li class="we">28<i>Sa</i></li><li class="we">29<i>So</i></li>
      <li>30<i>Mo</i><b>5</b></li><li>31<i>Di</i></li>
    </ul>
    <!-- Februar -->
    <ul class="month">
      <li>1<i>Mi</i><b>5</b></li><li>2<i>Do</i></li><li>3<i>Fr</i></li><li class="we">4<i>Sa</i></li><li class="we">5<i>So</i></li>
      <li>6<i>Mo</i><b>6</b></li><li>7<i>Di</i></li><li>8<i>Mi</i></li><li>9<i>Do</i></li><li>10<i>Fr</i></li>
      <li class="we">11<i>Sa</i></li><li class="we">12<i>So</i></li>
      <li>13<i>Mo</i><b>7</b></li><li>14<i>Di</i></li><li>15<i>Mi</i></li><li>16<i>Do</i></li><li>17<i>Fr</i></li>
      <li class="we">18<i>Sa</i></li><li class="we">19<i>So</i></li>
      <li>20<i>Mo</i><b>8</b></li><li>21<i>Di</i></li><li>22<i>Mi</i></li><li>23<i>Do</i></li><li>24<i>Fr</i></li>
      <li class="we">25<i>Sa</i></li><li class="we">26<i>So</i></li>
      <li>27<i>Mo</i><b>9</b></li><li>28<i>Di</i></li><li></li><li></li><li></li>
    </ul>
    <!-- März -->
    <ul class="month">
      <li>1<i>Mi</i><b>9</b></li><li>2<i>Do</i></li><li>3<i>Fr</i></li><li class="we">4<i>Sa</i></li><li class="we">5<i>So</i></li>
      <li>6<i>Mo</i><b>10</b></li><li>7<i>Di</i></li><li class="hol">8<i>Mi</i><s>Int. Frauentag *</s></li><li>9<i>Do</i></li><li>10<i>Fr</i></li>
      <li class="we">11<i>Sa</i></li><li class="we">12<i>So</i></li>
      <li>13<i>Mo</i><b>11</b></li><li>14<i>Di</i></li><li>15<i>Mi</i></li><li>16<i>Do</i></li><li>17<i>Fr</i></li>
      <li class="we">18<i>Sa</i></li><li class="we">19<i>So</i></li>
      <li>20<i>Mo</i><b>12</b></li><li>21<i>Di</i></li><li>22<i>Mi</i></li><li>23<i>Do</i></li><li>24<i>Fr</i></li>
      <li class="we">25<i>Sa</i></li><li class="we">26<i>So</i></li>
      <li>27<i>Mo</i><b>13</b></li><li>28<i>Di</i></li><li>29<i>Mi</i></li><li>30<i>Do</i></li><li>31<i>Fr</i></li>
    </ul>
    <!-- April -->
    <ul class="month">
      <li class="we">1<i>Sa</i></li><li class="we">2<i>So</i></li>
      <li>3<i>Mo</i><b>14</b></li><li>4<i>Di</i></li><li>5<i>Mi</i></li><li>6<i>Do</i></li><li class="hol">7<i>Fr</i><s>Karfreitag</s></li>
      <li class="we">8<i>Sa</i></li><li class="we hol">9<i>So</i><s>Ostersonntag *</s></li>
      <li class="hol">10<i>Mo</i><s>Ostermontag</s></li><li>11<i>Di</i><b>15</b></li><li>12<i>Mi</i></li><li>13<i>Do</i></li><li>14<i>Fr</i></li>
      <li class="we">15<i>Sa</i></li><li class="we">16<i>So</i></li>
      <li>17<i>Mo</i><b>16</b></li><li>18<i>Di</i></li><li>19<i>Mi</i></li><li>20<i>Do</i></li><li>21<i>Fr</i></li>
      <li class="we">22<i>Sa</i></li><li class="we">23<i>So</i></li>
      <li>24<i>Mo</i><b>17</b></li><li>25<i>Di</i></li><li>26<i>Mi</i></li><li>27<i>Do</i></li><li>28<i>Fr</i></li>
      <li class="we">29<i>Sa</i></li><li class="we">30<i>So</i></li><li></li>
    </ul>
    <!-- Mai -->
    <ul class="month">
      <li class="hol">1<i>Mo</i><s>Maifeiertag</s></li><li>2<i>Di</i><b>18</b></li><li>3<i>Mi</i></li><li>4<i>Do</i></li><li>5<i>Fr</i></li>
      <li class="we">6<i>Sa</i></li><li class="we">7<i>So</i></li>
      <li>8<i>Mo</i><b>19</b></li><li>9<i>Di</i></li><li>10<i>Mi</i></li><li>11<i>Do</i></li><li>12<i>Fr</i></li>
      <li class="we">13<i>Sa</i></li><li class="we">14<i>So</i></li>
      <li>15<i>Mo</i><b>20</b></li><li>16<i>Di</i></li><li>17<i>Mi</i></li><li class="hol">18<i>Do</i><s>Christi Himmelfahrt</s></li><li>19<i>Fr</i></li>
      <li class="we">20<i>Sa</i></li><li class="we">21<i>So</i></li>
      <li>22<i>Mo</i><b>21</b></li><li>23<i>Di</i></li><li>24<i>Mi</i></li><li>25<i>Do</i></li><li>26<i>Fr</i></li>
      <li class="we">27<i>Sa</i></li><li class="we hol">28<i>So</i><s>Pfingstsonntag *</s></li>
      <li class="hol">29<i>Mo</i><s>Pfingstmontag</s></li><li>30<i>Di</i><b>22</b></li><li>31<i>Mi</i></li>
    </ul>
    <!-- Juni -->
    <ul class="month">
      <li>1<i>Do</i><b>22</b></li><li>2<i>Fr</i></li><li class="we">3<i>Sa</i></li><li class="we">4<i>So</i></li>
      <li>5<i>Mo</i><b>23</b></li><li>6<i>Di</i></li><li>7<i>Mi</i></li><li class="hol">8<i>Do</i><s>Fronleichnam *</s></li><li>9<i>Fr</i></li>
      <li class="we">10<i>Sa</i></li><li class="we">11<i>So</i></li>
      <li>12<i>Mo</i><b>24</b></li><li>13<i>Di</i></li><li>14<i>Mi</i></li><li>15<i>Do</i></li><li>16<i>Fr</i></li>
      <li class="we">17<i>Sa</i></li><li class="we">18<i>So</i></li>
      <li>19<i>Mo</i><b>25</b></li><li>20<i>Di</i></li><li>21<i>Mi</i></li><li>22<i>Do</i></li><li>23<i>Fr</i></li>
      <li class="we">24<i>Sa</i></li><li class="we">25<i>So</i></li>
      <li>26<i>Mo</i><b>26</b></li><li>27<i>Di</i></li><li>28<i>Mi</i></li><li>29<i>Do</i></li><li>30<i>Fr</i></li><li></li>
    </ul>
    <!-- Juli -->
    <ul class="month">
      <li class="we">1<i>Sa</i></li><li class="we">2<i>So</i></li>
      <li>3<i>Mo</i><b>27</b></li><li>4<i>Di</i></li><li>5<i>Mi</i></li><li>6<i>Do</i></li><li>7<i>Fr</i></li>
      <li class="we">8<i>Sa</i></li><li class="we">9<i>So</i></li>
      <li>10<i>Mo</i><b>28</b></li><li>11<i>Di</i></li><li>12<i>Mi</i></li><li>13<i>Do</i></li><li>14<i>Fr</i></li>
      <li class="we">15<i>Sa</i></li><li class="we">16<i>So</i></li>
      <li>17<i>Mo</i><b>29</b></li><li>18<i>Di</i></li><li>19<i>Mi</i></li><li>20<i>Do</i></li><li>21<i>Fr</i></li>
      <li class="we">22<i>Sa</i></li><li class="we">23<i>So</i></li>
      <li>24<i>Mo</i><b>30</b></li><li>25<i>Di</i></li><li>26<i>Mi</i></li><li>27<i>Do</i></li><li>28<i>Fr</i></li>
      <li class="we">29<i>Sa</i></li><li class="we">30<i>So</i></li>
      <li>31<i>Mo</i></li>
    </ul>
    <!-- August -->
    <ul class="month">
      <li>1<i>Di</i><b>31</b></li><li>2<i>Mi</i></li><li>3<i>Do</i></li><li>4<i>Fr</i></li><li class="we">5<i>Sa</i></li><li class="we">6<i>So</i></li>
      <li>7<i>Mo</i><b>32</b></li><li>8<i>Di</i></li><li>9<i>Mi</i></li><li>10<i>Do</i></li><li>11<i>Fr</i></li>
      <li class="we">12<i>Sa</i></li><li class="we">13<i>So</i></li>
      <li>14<i>Mo</i></li><li class="hol">15<i>Di</i><s>Mariä Himmelfahrt *</s></li><li>16<i>Mi</i><b>33</b></li><li>17<i>Do</i></li><li>18<i>Fr</i></li>
      <li class="we">19<i>Sa</i></li><li class="we">20<i>So</i></li>
      <li>21<i>Mo</i><b>34</b></li><li>22<i>Di</i></li><li>23<i>Mi</i></li><li>24<i>Do</i></li><li>25<i>Fr</i></li>
      <li class="we">26<i>Sa</i></li><li class="we">27<i>So</i></li>
      <li>28<i>Mo</i><b>35</b></li><li>29<i>Di</i></li><li>30<i>Mi</i></li><li>31<i>Do</i></li>
    </ul>
    <!-- September -->
    <ul class="month">
      <li>1<i>Fr</i></li><li class="we">2<i>Sa</i></li><li class="we">3<i>So</i></li>
      <li>4<i>Mo</i><b>36</b></li><li>5<i>Di</i></li><li>6<i>Mi</i></li><li>7<i>Do</i></li><li>8<i>Fr</i></li>
      <li class="we">9<i>Sa</i></li><li class="we">10<i>So</i></li>
      <li>11<i>Mo</i><b>37</b></li><li>12<i>Di</i></li><li>13<i>Mi</i></li><li>14<i>Do</i></li><li>15<i>Fr</i></li>
      <li class="we">16<i>Sa</i></li><li class="we">17<i>So</i></li>
      <li>18<i>Mo</i><b>38</b></li><li>19<i>Di</i></li><li class="hol">20<i>Mi</i><s>Weltkindertag *</s></li><li>21<i>Do</i></li><li>22<i>Fr</i></li>
      <li class="we">23<i>Sa</i></li><li class="we">24<i>So</i></li>
      <li>25<i>Mo</i><b>39</b></li><li>26<i>Di</i></li><li>27<i>Mi</i></li><li>28<i>Do</i></li><li>29<i>Fr</i></li>
      <li class="we">30<i>Sa</i></li><li></li>
    </ul>
    <!-- Oktober -->
    <ul class="month">
      <li class="we">1<i>So</i></li>
      <li>2<i>Mo</i></li><li class="hol">3<i>Di</i><s>Tag der Dt. Einheit</s></li><li>4<i>Mi</i><b>40</b></li><li>5<i>Do</i></li><li>6<i>Fr</i></li>
      <li class="we">7<i>Sa</i></li><li class="we">8<i>So</i></li>
      <li>9<i>Mo</i><b>41</b></li><li>10<i>Di</i></li><li>11<i>Mi</i></li><li>12<i>Do</i></li><li>13<i>Fr</i></li>
      <li class="we">14<i>Sa</i></li><li class="we">15<i>So</i></li>
      <li>16<i>Mo</i><b>42</b></li><li>17<i>Di</i></li><li>18<i>Mi</i></li><li>19<i>Do</i></li><li>20<i>Fr</i></li>
      <li class="we">21<i>Sa</i></li><li class="we">22<i>So</i></li>
      <li>23<i>Mo</i><b>43</b></li><li>24<i>Di</i></li><li>25<i>Mi</i></li><li>26<i>Do</i></li><li>27<i>Fr</i></li>
      <li class="we">28<i>Sa</i></li><li class="we">29<i>So</i></li>
      <li>30<i>Mo</i></li><li class="hol">31<i>Di</i><s>Reformationstag</s></li>
    </ul>
    <!-- November -->
    <ul class="month">
      <li class="hol">1<i>Mi</i><s>Allerheiligen *</s></li><li>2<i>Do</i><b>44</b></li><li>3<i>Fr</i></li><li class="we">4<i>Sa</i></li><li class="we">5<i>So</i></li>
      <li>6<i>Mo</i><b>45</b></li><li>7<i>Di</i></li><li>8<i>Mi</i></li><li>9<i>Do</i></li><li>10<i>Fr</i></li>
      <li class="we">11<i>Sa</i></li><li class="we">12<i>So</i></li>
      <li>13<i>Mo</i><b>46</b></li><li>14<i>Di</i></li><li>15<i>Mi</i></li><li>16<i>Do</i></li><li>17<i>Fr</i></li>
      <li class="we">18<i>Sa</i></li><li class="we">19<i>So</i></li>
      <li>20<i>Mo</i><b>47</b></li><li>21<i>Di</i></li><li class="hol">22<i>Mi</i><s>Buß- und Bettag *</s></li><li>23<i>Do</i></li><li>24<i>Fr</i></li>
      <li class="we">25<i>Sa</i></li><li class="we">26<i>So</i></li>
      <li>27<i>Mo</i><b>48</b></li><li>28<i>Di</i></li><li>29<i>Mi</i></li><li>30<i>Do</i></li><li></li>
    </ul>
    <!-- Dezember -->
    <ul class="month">
      <li>1<i>Fr</i></li><li class="we">2<i>Sa</i></li><li class="we">3<i>So</i></li>
      <li>4<i>Mo</i><b>49</b></li><li>5<i>Di</i></li><li>6<i>Mi</i></li><li>7<i>Do</i></li><li>8<i>Fr</i></li>
      <li class="we">9<i>Sa</i></li><li class="we">10<i>So</i></li>
      <li>11<i>Mo</i><b>50</b></li><li>12<i>Di</i></li><li>13<i>Mi</i></li><li>14<i>Do</i></li><li>15<i>Fr</i></li>
      <li class="we">16<i>Sa</i></li><li class="we">17<i>So</i></li>
      <li>18<i>Mo</i><b>51</b></li><li>19<i>Di</i></li><li>20<i>Mi</i></li><li>21<i>Do</i></li><li>22<i>Fr</i></li>
      <li class="we">23<i>Sa</i></li><li class="we">24<i>So</i><s>Heiligabend</s></li>
      <li class="hol">25<i>Mo</i><s>1. Weihnachtstag</s></li><li class="hol">26<i>Di</i><s>2. Weihnachtstag</s></li><li>27<i>Mi</i><b>52</b></li><li>28<i>Do</i></li><li>29<i>Fr</i></li>
      <li class="we">30<i>Sa</i></li><li class="we">31<i>So</i><s>Silvester</s></li>
    </ul>
    <!-- Januar 2024 -->
    <ul class="month">
      <li class="hol">1<i>Mo</i><s>Neujahr</s></li><li>2<i>Di</i><b>1</b></li><li>3<i>Mi</i></li><li>4<i>Do</i></li><li>5<i>Fr</i></li>
      <li class="we hol">6<i>Sa</i><s>Heilige Drei Könige *</s></li><li class="we">7<i>So</i></li>
      <li>8<i>Mo</i><b>2</b></li><li>9<i>Di</i></li><li>10<i>Mi</i></li><li>11<i>Do</i></li><li>12<i>Fr</i></li>
      <li class="we">13<i>Sa</i></li><li class="we">14<i>So</i></li>
      <li>15<i>Mo</i><b>3</b></li><li>16<i>Di</i></li><li>17<i>Mi</i></li><li>18<i>Do</i></li><li>19<i>Fr</i></li>
      <li class="we">20<i>Sa</i></li><li class="we">21<i>So</i></li>
      <li>22<i>Mo</i><b>4</b></li><li>23<i>Di</i></li><li>24<i>Mi</i></li><li>25<i>Do</i></li><li>26<i>Fr</i></li>
      <li class="we">27<i>Sa</i></li><li class="we">28<i>So</i></li>
      <li>29<i>Mo</i><b>5</b></li><li>30<i>Di</i></li><li>31<i>Mi</i></li>
    </ul>
  </main>
</div>
</body>
</html>
```